Broschüre für Hausmeisterservice
Zielgruppe
Unser Hausmeisterservice bietet zuverlässige und professionelle Dienstleistungen rund um die Immobilie. Dazu gehören unter anderem die Pflege und Wartung von Gebäuden, kleinere Reparaturen, Reinigungsarbeiten, Gartenpflege sowie Winterdienst. Unser Ziel ist es, Eigentümern, Hausverwaltungen und Unternehmen einen sorgenfreien Rundum-Service zu bieten, damit ihre Immobilien stets gepflegt und funktionstüchtig sind. Unsere Zielgruppe sind somit Hausverwaltungen, Eigentümergemeinschaften, Firmen und Privatpersonen, die Wert auf eine gepflegte Immobilie legen und einen zuverlässigen Partner suchen.
Aufgabenstellung
Corporate Design und Kommunikation:
Freundlich, vertrauenswürdig und professionell wirken
Klare, verständliche Sprache verwenden
Visuelle Elemente, die Sauberkeit, Ordnung und gepflegte Immobilien ausstrahlen
Call-to-Action:
Klare Aufforderungen zur Kontaktaufnahme, Angebotserstellung oder Terminvereinbarung.

```html
<!DOCTYPE html>
<html lang="de">
<head>
<meta charset="utf-8">
<title>Hof &amp; Ordnung – Broschüre Hausmeisterservice</title>
<link rel="stylesheet" href="https://fonts.googleapis.com/css2?family=Montserrat:wght@600;700;800&family=Inter:wght@400;500;600&display=swap">
<style>
  :root{
    --navy:#143a5a;
    --navy-dark:#0f2e48;
    --green:#6aa43a;
    --green-light:#8cc152;
    --paper:#ffffff;
    --paper-shade:#f3f4f5;
    --ink:#1c2b3a;
    --muted:#5d6773;
    --bg:#e4e5e7;
  }
  *{box-sizing:border-box;margin:0;padding:0}
  html,body{width:1200px;height:678px;overflow:hidden;background:var(--bg)}
  body{font-family:"Inter",Arial,sans-serif;color:var(--ink)}

  .brochure{position:absolute;left:50px;top:54px;width:1100px;height:570px;display:flex;box-shadow:0 10px 30px rgba(0,0,0,.12)}

  /* Cover panel */
  .cover{position:relative;width:380px;height:100%;background:linear-gradient(90deg,var(--paper) 85%,var(--paper-shade));overflow:hidden}
  .cover-band{position:absolute;left:0;right:0;height:34px;background:var(--navy)}
  .cover-band.top{top:0}
  .cover-band.bottom{bottom:0}
  .cover-content{position:absolute;left:36px;right:30px;top:300px}
  .brand{display:flex;align-items:center;gap:14px}
  .brand-dot{width:34px;height:34px;border-radius:50%;background:var(--green);flex:none}
  .brand-name{font-family:"Montserrat",Arial,sans-serif;font-weight:800;font-size:40px;color:var(--navy);line-height:1}
  .tagline{font-family:"Montserrat",Arial,sans-serif;font-weight:700;font-size:20px;color:var(--navy);margin-top:10px}
  .tagline-sub{font-family:"Montserrat",Arial,sans-serif;font-weight:600;font-size:17px;color:var(--ink);margin-top:6px}
  .contact{margin-top:26px;display:flex;justify-content:space-between;align-items:flex-end}
  .contact-label{font-size:15px;font-weight:500;color:var(--ink)}
  .contact-phone{font-family:"Montserrat",Arial,sans-serif;font-weight:700;font-size:19px;color:var(--navy);margin-top:8px}
  .contact-icons{display:flex;gap:7px;margin-bottom:30px}
  .contact-icons svg{width:20px;height:20px}

  /* Photo panel */
  .photo{width:400px;height:100%;background:linear-gradient(180deg,#a9c6e3 0%,#d6e2ec 30%,#b8bec5 55%,#7fa56a 80%,#c9ccce 100%)}

  /* Info panel */
  .info{width:320px;height:100%;background:var(--paper);padding:34px 30px 28px 34px;display:flex;flex-direction:column}
  .info-title{font-family:"Montserrat",Arial,sans-serif;font-weight:800;font-size:21px;line-height:1.3;color:var(--ink);text-align:center}
  .section-label{font-family:"Montserrat",Arial,sans-serif;font-weight:700;font-size:13px;color:var(--green);margin-top:30px;padding-bottom:7px;border-bottom:2px solid var(--green)}
  .service-list{list-style:none;margin-top:16px;border-left:2px solid var(--green);padding-left:16px}
  .service{display:flex;align-items:center;gap:14px;margin-bottom:18px}
  .service-icon{width:44px;height:44px;border-radius:50%;border:2px solid var(--green);display:flex;align-items:center;justify-content:center;flex:none}
  .service-icon span{width:28px;height:28px;border-radius:50%;background:var(--green)}
  .service-text{font-size:12px;line-height:1.35;color:var(--muted)}
  .reason-text{font-size:12px;line-height:1.45;color:var(--muted);margin-top:12px}
  .cta{margin-top:auto;display:flex;align-items:center;gap:12px}
  .cta-button{flex:1;background:var(--green);color:#fff;font-family:"Montserrat",Arial,sans-serif;font-weight:700;font-size:14px;text-align:center;padding:10px 12px;border-radius:20px}
  .cta-arrow{width:32px;height:32px;border-radius:50%;background:var(--green);display:flex;align-items:center;justify-content:center}
  .web{font-size:12px;font-weight:600;color:var(--green);margin-top:12px;text-align:center}
</style>
</head>
<body>
<main class="brochure">
  <section class="cover">
    <div class="cover-band top"></div>
    <div class="cover-content">
      <div class="brand">
        <span class="brand-dot"></span>
        <h1 class="brand-name">Hof &amp; Ordnung</h1>
      </div>
      <p class="tagline">Hauswartung mit System</p>
      <p class="tagline-sub">mit Herz &amp; System</p>
      <div class="contact">
        <div>
          <p class="contact-label">Telefonberatung</p>
          <p class="contact-phone">Tel: 482936</p>
        </div>
        <div class="contact-icons">
          <svg viewBox="0 0 20 20"><circle cx="10" cy="10" r="10" fill="var(--navy)"/><path d="M7 5.5l1.6 2.3-1 1c.6 1.3 1.6 2.3 2.9 2.9l1-1 2.3 1.6-.8 1.7c-3.8-.3-6.6-3.1-6.9-6.9z" fill="#fff"/></svg>
          <svg viewBox="0 0 20 20"><circle cx="10" cy="10" r="10" fill="var(--navy)"/><rect x="5" y="6.5" width="10" height="7" rx="1" fill="none" stroke="#fff" stroke-width="1.3"/><path d="M5.3 7l4.7 3.5L14.7 7" fill="none" stroke="#fff" stroke-width="1.3"/></svg>
          <svg viewBox="0 0 20 20"><circle cx="10" cy="10" r="10" fill="var(--navy)"/><path d="M10 4.5a3.5 3.5 0 0 0-3.5 3.5c0 2.6 3.5 7 3.5 7s3.5-4.4 3.5-7A3.5 3.5 0 0 0 10 4.5z" fill="#fff"/><circle cx="10" cy="8" r="1.3" fill="var(--navy)"/></svg>
          <svg viewBox="0 0 20 20"><circle cx="10" cy="10" r="10" fill="var(--navy)"/><circle cx="10" cy="10" r="5" fill="none" stroke="#fff" stroke-width="1.3"/><path d="M10 7v3.2l2 1.3" fill="none" stroke="#fff" stroke-width="1.3"/></svg>
        </div>
      </div>
    </div>
    <div class="cover-band bottom"></div>
  </section>

  <div class="photo" role="img" aria-label="Foto eines modernen, gepflegten Mehrfamilienhauses mit Balkonen, Rasen und Bäumen unter blauem Himmel"></div>

  <section class="info">
    <h2 class="info-title">Hausmeisterservice<br>jetzt Termin<br>vereinbaren!</h2>
    <p class="section-label">Leistungen im Überblick</p>
    <ul class="service-list">
      <li class="service"><span class="service-icon"><span></span></span><p class="service-text">Reparaturen und Wartung am Gebäude</p></li>
      <li class="service"><span class="service-icon"><span></span></span><p class="service-text">Garten- und Winterdienst zuverlässig</p></li>
    </ul>
    <p class="section-label">Warum wir überzeugen</p>
    <p class="reason-text">Feste Ansprechpartner, klare Preise und schnelle Reaktion.</p>
    <div class="cta">
      <span class="cta-button">Angebot anfordern</span>
      <span class="cta-arrow"><svg width="16" height="16" viewBox="0 0 16 16"><path d="M3 8h9M8.5 4.5L12 8l-3.5 3.5" fill="none" stroke="#fff" stroke-width="2" stroke-linecap="round"/></svg></span>
    </div>
    <p class="web">www.hof-ordnung.example</p>
  </section>
</main>
</body>
</html>
```